Brasolina! Poster

I need a poster for an event to be staged in Gibraltar called Brasolina!
Brasolina! is a food festival and street party that celebrates GIbraltar's multicultural and colour community. The event has a tagline "Flavours of the Warm Bowl".
I am looking for a poster which captures the spirit of the event without being too obvious.
Updates

Because this event is rapidly approaching I would like to settle the design for the poster as soon as possible, so the earlier you post the better
thanks

I am trying to avoid a poster that looks too similar to last year's.
Red and White are Gibraltar's national colours and I would like to feature them in the design.
Brasolina! the name needs to be in Clarendon! (bold) with tight character spacing

Target Market(s)

Target market are the people of Gibraltar - Gibraltar is a british colony in southern Spain, population 30,000 - Gibraltarians are of British, Spanish, Italian (Genoa), Portugese and Moroccan extraction. Gibraltar also has large Hindu, Jewish and Moroccan Communities.

Industry/Entity Type

Events

Requirements
Must have
• Initially I am looking for an A2 design - we will use the same design themes for the website and also base a 120cm x 90cm banner on the design.
• Must have t
• "HearsayStagesLive.com" "Brasolina!" , "Flavours of the Warm Bowl", Friday June 19th 2009, Ropewalk Plaza, Starts 21.00 hrs Finishes 0100 hrs, Free Entry, Everyone Welcome, Firework and Laser Display at 22.30 hrs
• My company logo, Office of Heritage Bloom Fair Logo
• Title must use Clarendon font
Nice to have
• Could be a photo or an illustration nothing that too obviously reflects the theme, doesn''t need to have all or anymore than one of the main Gibraltarian cultures
Should not have
• picture of the ROck of Gibaltar, Money, bad photography in particular bad food photography, just a picture of some food

```html
<!DOCTYPE html>
<html lang="en">
<head>
<meta charset="utf-8">
<title>Brasolina! Poster</title>
<link rel="stylesheet" href="https://fonts.googleapis.com/css2?family=Roboto+Slab:wght@700;800&family=Roboto+Condensed:wght@400;700&family=Archivo:wght@500&display=swap">
<style>
  :root {
    --red: #ee3b36;
    --title-red: #e8312c;
    --ink: #1a1a1a;
    --white: #ffffff;
    --partner-blue: #2f8fd0;
    --photo-warm: #e6b3a8;
    --photo-mid: #d9876a;
    --photo-leaf: #9cc46a;
  }
  * { margin: 0; padding: 0; box-sizing: border-box; }
  html, body { width: 1200px; height: 908px; overflow: hidden; background: var(--white); }
  .poster { position: relative; width: 1200px; height: 908px; background: var(--white); overflow: hidden; }

  .crop-marks { position: absolute; inset: 0; }

  .site-band {
    position: absolute; left: 18px; top: 18px; width: 1164px; height: 48px;
    background: var(--red);
    display: flex; align-items: center; padding-left: 61px;
  }
  .site-band__url {
    color: var(--white); font-family: "Roboto Condensed", sans-serif; font-weight: 700;
    font-size: 18px; letter-spacing: 5px;
  }

  .feature-photo {
    position: absolute; left: 640px; top: 66px; width: 542px; height: 740px;
    background: radial-gradient(ellipse 62% 60% at 72% 48%,
      var(--photo-warm) 0%, var(--photo-mid) 38%, var(--photo-leaf) 62%, rgba(255,255,255,0) 100%);
  }

  .title {
    position: absolute; left: 74px; top: 262px;
    font-family: "Roboto Slab", serif; font-weight: 800;
    font-size: 108px; line-height: 1; letter-spacing: -3px;
    color: var(--title-red);
  }

  .subtitle {
    position: absolute; left: 82px; top: 388px;
    display: flex; align-items: stretch;
  }
  .subtitle__kind {
    font-family: "Archivo", sans-serif; font-weight: 500;
    font-size: 28px; line-height: 39px; letter-spacing: 2px; color: var(--ink);
    padding-right: 10px; border-right: 2px solid var(--red);
  }
  .subtitle__tagline {
    font-family: "Roboto Condensed", sans-serif; font-weight: 700;
    font-size: 31px; line-height: 39px; letter-spacing: 2.5px; color: var(--ink);
    padding-left: 12px;
  }

  .event-details {
    position: absolute; left: 74px; top: 684px; width: 616px; height: 180px;
    background: linear-gradient(90deg, var(--red) 0%, #f59a88 45%, #fbe3dc 75%, rgba(255,255,255,0) 100%);
    font-family: "Roboto Condensed", sans-serif; font-weight: 700;
    font-size: 18px; color: var(--ink);
  }
  .event-details__row { padding: 0 16px; }
  .event-details__row--when { height: 70px; padding-top: 12px; line-height: 24px; border-bottom: 3px solid var(--white); }
  .event-details__row--entry { height: 57px; line-height: 54px; border-bottom: 3px solid var(--white); }
  .event-details__row--show { height: 53px; line-height: 52px; }

  .partner-name {
    position: absolute; left: 756px; top: 792px; width: 150px;
    font-family: "Roboto Condensed", sans-serif; font-weight: 700;
    font-size: 18px; line-height: 21px; color: var(--partner-blue);
  }

  .promoter-name {
    position: absolute; left: 974px; top: 832px;
    display: flex; align-items: center; gap: 8px;
    font-family: "Roboto Condensed", sans-serif; font-weight: 700;
    font-size: 17px; letter-spacing: 1.5px; color: var(--ink);
  }
  .promoter-name__dot { width: 14px; height: 14px; border-radius: 50%; background: var(--ink); }
</style>
</head>
<body>
<div class="poster">
  <svg class="crop-marks" width="1200" height="908" aria-hidden="true">
    <g stroke="#9a9a9a" stroke-width="1">
      <line x1="0" y1="18" x2="10" y2="18"/><line x1="18" y1="0" x2="18" y2="10"/>
      <line x1="1190" y1="18" x2="1200" y2="18"/><line x1="1182" y1="0" x2="1182" y2="10"/>
      <line x1="0" y1="890" x2="10" y2="890"/><line x1="18" y1="898" x2="18" y2="908"/>
      <line x1="1190" y1="890" x2="1200" y2="890"/><line x1="1182" y1="898" x2="1182" y2="908"/>
    </g>
  </svg>

  <header class="site-band">
    <span class="site-band__url">HearsayStagesLive.com</span>
  </header>

  <div class="feature-photo" role="img" aria-label="Close-up photo of an open sandwich with lettuce, rolled ham, cheese, tomato and parsley on a bread roll"></div>

  <h1 class="title">Brasolina!</h1>

  <div class="subtitle">
    <p class="subtitle__kind">FOOD FESTIVAL<br>STREET PARTY</p>
    <p class="subtitle__tagline">Flavours of the<br>Warm Bowl</p>
  </div>

  <section class="event-details">
    <p class="event-details__row event-details__row--when">Friday June 19th 2009, Ropewalk Plaza,<br>Starts 21.00 hrs Finishes 0100 hrs,</p>
    <p class="event-details__row event-details__row--entry">Free Entry, Everyone Welcome,</p>
    <p class="event-details__row event-details__row--show">Firework and Laser Display at 22.30 hrs</p>
  </section>

  <p class="partner-name">Office of Heritage Bloom Fair</p>

  <p class="promoter-name"><span class="promoter-name__dot"></span>HEARSAY STAGES</p>
</div>
</body>
</html>
```